Company or website name
- The Steadfast Haulers and Storage
- Links to the website
- Brightcarryhaul.com
- Describe your company and organization and target audience
- Residential and commercial moving and relocation service that needs a website redesign.
- The design should have the following
- I NEED THE WEBSITE TO BE SIMPLE AND STRAIGHT TO THE POINT...MAIN CONCERN IS THAT THEY FILL OUT INFORMATION TO GET QUOTE. SITE EXAMPLE THAT I LIKE IS ( WWW.GOTORVALE.COM) https://www.quornhaulwaysco.com/

```html
<!DOCTYPE html>
<html lang="en">
<head>
<meta charset="utf-8">
<title>The Steadfast Haulers and Storage — Moving and Storage Services</title>
<link href="https://fonts.googleapis.com/css2?family=Montserrat:wght@400;500;600;700&display=swap" rel="stylesheet">
<style>
:root{
  --green:#76c51f;
  --green-icon:#7ac943;
  --forest:#3f6a4e;
  --forest-dark:#2b4937;
  --ink:#1c1c1c;
  --muted:#8a8a8a;
  --soft-bg:#f5f5f5;
  --white:#ffffff;
  --line:#cfd8d1;
}
*{margin:0;padding:0;box-sizing:border-box}
html,body{width:1200px;height:4326px;overflow:hidden}
body{position:relative;font-family:'Montserrat',sans-serif;color:var(--ink);background:var(--white)}
.abs{position:absolute}

/* hero */
.hero{position:absolute;left:0;top:0;width:1200px;height:641px;overflow:hidden}
.hero-photo{position:absolute;left:0;top:0;width:688px;height:641px;background:linear-gradient(160deg,#5e7a66 0%,#4c6856 45%,#3f5a48 100%)}
.hero-side{position:absolute;left:688px;top:0;width:512px;height:641px;background:linear-gradient(180deg,#eef1ee,#e2e7e3)}
.brand{display:flex;align-items:center;gap:8px;color:var(--white);font-weight:600;font-size:18px;white-space:nowrap}
.brand-mark{width:14px;height:14px;background:var(--white)}
.nav{left:307px;top:34px;font-size:15px;color:#e8efe9}
.nav a{position:absolute;white-space:nowrap;text-decoration:none;color:inherit}
.nav a.active{color:var(--white);font-weight:600;border-bottom:2px solid var(--white);padding-bottom:4px}
.hero-title{left:117px;top:194px;font-size:42px;line-height:54px;font-weight:700;color:var(--white)}
.hero-sub{left:117px;top:311px;font-size:16px;color:#edf2ee}
.btn{display:flex;align-items:center;justify-content:center;background:var(--green);color:var(--white);font-weight:600;text-decoration:none}
.hero-btn{left:117px;top:384px;width:208px;height:44px;font-size:15px;color:#1f3b16}
.close{left:700px;top:9px;width:24px;height:24px}

.quote-card{position:absolute;left:725px;top:0;width:475px;height:541px;background:var(--white)}
.quote-title{left:32px;top:60px;font-size:15px;font-weight:600;border-bottom:2px solid var(--ink);padding-bottom:6px}
.quote-phone{left:287px;top:64px;font-size:14px;color:var(--forest);display:flex;gap:6px;align-items:center}
.tab{position:absolute;top:134px;width:108px;height:56px;display:flex;flex-direction:column;align-items:center;justify-content:flex-end;gap:6px;font-size:11px;color:var(--muted);padding-bottom:6px}
.tab.active{color:var(--ink);box-shadow:0 -2px 10px rgba(0,0,0,.07);background:var(--white)}
.field-label{position:absolute;font-size:11px;color:var(--ink)}
.field{position:absolute;width:186px;height:30px;border:1px solid var(--line);border-radius:4px;font-size:9px;color:#a5a5a5;padding:9px 16px}
.form-btn{position:absolute;top:443px;width:186px;height:39px;font-size:11px;font-weight:700;border-radius:3px}
.form-btn.outline{background:var(--white);border:1.5px solid var(--green);color:var(--green)}
.form-note{left:32px;top:504px;font-size:8px;color:var(--green)}

/* about */
.about-photo{left:65px;top:764px;width:460px;height:391px;background:linear-gradient(135deg,#c9b79a 0%,#d9cfc0 45%,#9fa39a 100%);z-index:2}
.about-block{left:35px;top:970px;width:210px;height:225px;background:#5a7e68}
.h2{font-size:34px;line-height:42px;font-weight:700;color:var(--ink)}
.about-title{left:601px;top:764px;font-size:32px}
.check-row{position:absolute;left:603px;display:flex;gap:30px;align-items:flex-start}
.check-row p{font-size:13px;line-height:16px;color:var(--muted);width:360px;padding-top:2px}
.more-link{left:912px;top:1160px;font-size:16px;font-weight:600;color:var(--green);border-bottom:2px solid var(--green);padding-bottom:4px}

/* services */
.services{position:absolute;left:0;top:1289px;width:1200px;height:937px;background:var(--soft-bg)}
.services-title{left:117px;top:93px}
.services-sub{left:117px;top:146px;font-size:12px;line-height:17px;color:var(--muted);width:360px}
.svc{position:absolute;width:313px;height:232px;display:flex;flex-direction:column;align-items:center;justify-content:flex-end;padding-bottom:30px;color:var(--white);font-weight:600;font-size:20px}
.svc.featured{background:var(--forest);justify-content:center;padding-bottom:0}
.svc.featured p{font-size:12px;font-weight:400;text-align:center;line-height:19px;margin-top:12px;color:#e6eee8}
.svc.featured a{font-size:12px;font-weight:500;color:var(--white);margin-top:8px;border-bottom:1px solid var(--white)}
.svc-btn{left:477px;top:801px;width:248px;height:60px;font-size:20px}

/* testimonials */
.reviews{position:absolute;left:0;top:2226px;width:1200px;height:482px;background:linear-gradient(180deg,#3c5043 0%,#2f4237 60%,#2a3b31 100%);overflow:hidden}
.reviews-title{left:117px;top:94px;color:var(--white)}
.review{position:absolute;top:183px;width:494px;height:181px;background:rgba(255,255,255,.22);border-radius:6px;padding:26px 38px;color:var(--white)}
.review p{font-size:14px;line-height:20px;font-weight:500}
.review-meta{display:flex;align-items:center;gap:10px;margin-top:14px}
.avatar{width:36px;height:36px;border-radius:50%;background:#c6c6c6}
.review-date{font-size:11px}
.review-name{font-size:14px;font-weight:600}
.stars{margin-left:auto;display:flex;gap:6px}
.dot{position:absolute;top:406px;width:20px;height:20px;border-radius:50%;border:1.5px solid #cfd7d0}
.dot.on{border-color:var(--green);background:radial-gradient(circle,var(--green) 45%,transparent 50%)}

/* features */
.features-title{left:117px;top:2800px}
.feat{position:absolute;width:230px}
.feat svg{display:block;width:52px;height:52px}
.feat h3{font-size:20px;font-weight:600;margin-top:16px;color:var(--ink)}
.feat p{font-size:12px;line-height:16px;color:var(--muted);margin-top:14px;width:180px}
.feat.highlight{background:var(--forest);padding:20px 14px;width:230px;height:199px}
.feat.highlight h3,.feat.highlight p{color:var(--white)}

/* cta */
.cta{position:absolute;left:0;top:3514px;width:1200px;height:233px;background:var(--forest)}
.cta-title{left:117px;top:90px;font-size:34px;line-height:42px;font-weight:700;color:var(--white)}
.cta-btn{left:744px;top:87px;width:304px;height:62px;font-size:20px}

/* partners */
.partners{position:absolute;left:0;top:3747px;width:1200px;height:124px;display:flex;align-items:center;justify-content:space-around;padding:0 105px}
.badge{height:26px;background:#c7c7c7;border-radius:4px}

/* footer */
.footer{position:absolute;left:0;top:3871px;width:1200px;height:455px;background:var(--forest-dark);color:var(--white)}
.footer .brand{left:126px;top:94px;position:absolute;font-size:20px}
.foot-h{position:absolute;top:80px;font-size:20px;font-weight:600}
.foot-links{position:absolute;left:455px;top:134px;list-style:none}
.foot-links li{font-size:16px;height:42px}
.foot-text{left:690px;top:137px;font-size:13px;line-height:24px;width:400px;color:#e3ebe5}
.subscribe{left:690px;top:199px;width:395px;height:43px;background:#5c7866;border-radius:4px}
.subscribe-btn{position:absolute;right:0;top:0;width:106px;height:43px;font-size:13px;font-weight:700;border-radius:0 4px 4px 0}
.social{position:absolute;top:292px;width:33px;height:33px;border:3px solid var(--green-icon);border-radius:7px}
</style>
</head>
<body>

<section class="hero">
  <div class="hero-photo" role="img" aria-label="Moving truck on a road under a green tone"></div>
  <div class="hero-side" role="img" aria-label="Faded street scene behind the quote form"></div>

  <div class="abs brand" style="left:117px;top:32px"><span class="brand-mark"></span>Steadfast Haulers</div>
  <nav class="abs nav">
    <a class="active" style="left:0">Home</a>
    <a style="left:76px">Services</a>
    <a style="left:168px">Offices</a>
    <a style="left:250px">Contact</a>
  </nav>

  <h1 class="abs hero-title">Get Move And Storage<br>Services Solutions !</h1>
  <p class="abs hero-sub">Accelerated delivery, Discount Rates, And Free Move Plans</p>
  <a class="abs btn hero-btn">Check Our Services</a>

  <svg class="abs close" viewBox="0 0 24 24"><circle cx="12" cy="12" r="10" fill="none" stroke="#8a8a8a" stroke-width="1.6"/><path d="M8 8l8 8M16 8l-8 8" stroke="#8a8a8a" stroke-width="1.6"/></svg>

  <form class="quote-card">
    <div class="abs quote-title">Moving Qoute</div>
    <div class="abs quote-phone">
      <svg width="16" height="16" viewBox="0 0 24 24"><path d="M5 3h4l2 5-3 2a11 11 0 006 6l2-3 5 2v4a2 2 0 01-2 2A17 17 0 013 5a2 2 0 012-2z" fill="none" stroke="#3f6a4e" stroke-width="2"/></svg>
      +18 77 613 905
    </div>

    <div class="tab active" style="left:35px">
      <svg width="26" height="22" viewBox="0 0 26 22"><path d="M13 1L1 11h4v10h6v-6h4v6h6V11h4z" fill="#1c1c1c"/></svg>Residential
    </div>
    <div class="tab" style="left:176px">
      <svg width="26" height="22" viewBox="0 0 26 22"><rect x="3" y="3" width="20" height="18" rx="2" fill="#8a8a8a"/><path d="M7 9h12M7 13h12M7 17h12" stroke="#fff" stroke-width="1.5"/></svg>Office
    </div>
    <div class="tab" style="left:306px">
      <svg width="26" height="22" viewBox="0 0 26 22"><rect x="4" y="2" width="18" height="19" fill="#8a8a8a"/><path d="M4 8h18M11 5h4" stroke="#fff" stroke-width="1.5"/></svg>Storage
    </div>

    <label class="field-label" style="left:32px;top:221px">Moving From*</label>
    <div class="field" style="left:32px;top:240px">ZIP Code Required</div>
    <label class="field-label" style="left:232px;top:221px">Moving To*</label>
    <div class="field" style="left:232px;top:240px">ZIP Code Required</div>

    <label class="field-label" style="left:32px;top:293px">Moving Date*</label>
    <div class="field" style="left:32px;top:312px">22/03/2022</div>
    <label class="field-label" style="left:232px;top:293px">Full Name*</label>
    <div class="field" style="left:232px;top:312px">Your Full Name</div>

    <label class="field-label" style="left:32px;top:364px">Your Email*</label>
    <div class="field" style="left:32px;top:383px">name@mailbox.com</div>
    <label class="field-label" style="left:232px;top:364px">Your Phone*</label>
    <div class="field" style="left:232px;top:383px">6281700000000</div>

    <a class="btn form-btn" style="left:32px">Free Quote</a>
    <a class="btn form-btn outline" style="left:232px">Make Reservation</a>
    <p class="abs form-note">Steadfast Moving Solutions agent will be e-mailing you a quote in 24 hours or less</p>
  </form>
</section>

<section>
  <div class="abs about-block"></div>
  <div class="abs about-photo" role="img" aria-label="Couple relaxing on a sofa among moving boxes"></div>
  <h2 class="abs h2 about-title">Safe, Reliable And Express<br>Solutions With Steadfast</h2>

  <div class="check-row" style="top:868px"><svg width="36" height="34" viewBox="0 0 36 34"><path d="M28 15v15H3V5h20" fill="none" stroke="#7ac943" stroke-width="2.5"/><path d="M9 16l6 6L33 3" fill="none" stroke="#7ac943" stroke-width="2.5"/></svg><p>We're a stress-free moving company. Our goal is to get you moved easily efficiently.</p></div>
  <div class="check-row" style="top:921px"><svg width="36" height="34" viewBox="0 0 36 34"><path d="M28 15v15H3V5h20" fill="none" stroke="#7ac943" stroke-width="2.5"/><path d="M9 16l6 6L33 3" fill="none" stroke="#7ac943" stroke-width="2.5"/></svg><p>We can handle any job, from one-room apartments to expansive estates.</p></div>
  <div class="check-row" style="top:974px"><svg width="36" height="34" viewBox="0 0 36 34"><path d="M28 15v15H3V5h20" fill="none" stroke="#7ac943" stroke-width="2.5"/><path d="M9 16l6 6L33 3" fill="none" stroke="#7ac943" stroke-width="2.5"/></svg><p>Our team offers you convenient and affordable options for a completely stress-free experience.</p></div>
  <div class="check-row" style="top:1032px"><svg width="36" height="34" viewBox="0 0 36 34"><path d="M28 15v15H3V5h20" fill="none" stroke="#7ac943" stroke-width="2.5"/><path d="M9 16l6 6L33 3" fill="none" stroke="#7ac943" stroke-width="2.5"/></svg><p>Our reliable local movers live in the communities they serve. We're not just your movers, we're your neighbors.</p></div>
  <div class="check-row" style="top:1094px"><svg width="36" height="34" viewBox="0 0 36 34"><path d="M28 15v15H3V5h20" fill="none" stroke="#7ac943" stroke-width="2.5"/><path d="M9 16l6 6L33 3" fill="none" stroke="#7ac943" stroke-width="2.5"/></svg><p>Our trained, professional movers undergo rigorous background checks to maintain quality.</p></div>

  <a class="abs more-link">More About Us</a>
</section>

<section class="services">
  <h2 class="abs h2 services-title">How We Can Help ?</h2>
  <p class="abs services-sub">We're a stress-free moving company. Our goal is to get you moved easily efficiently.</p>

  <div class="svc featured" style="left:117px;top:237px">Residential<p>Lorem ipsum sit dolor amet della<br>rapisota daeltarso subdiso</p><a>Learn More</a></div>
  <div class="svc" style="left:445px;top:237px;background:linear-gradient(180deg,#a9a397,#5a5c55)" role="img" aria-label="Office desk with laptop and plants">Office</div>
  <div class="svc" style="left:771px;top:237px;background:linear-gradient(180deg,#a69f9b,#6a5a4c)" role="img" aria-label="Warehouse storage shelves with a forklift">Storage</div>
  <div class="svc" style="left:117px;top:484px;background:linear-gradient(180deg,#77706a,#3c3834)" role="img" aria-label="Movers packing household items">Local</div>
  <div class="svc" style="left:445px;top:484px;background:linear-gradient(180deg,#6f7f7a,#44483f)" role="img" aria-label="Long straight highway under a cloudy sky">Long Distance</div>
  <div class="svc" style="left:771px;top:484px;background:linear-gradient(180deg,#9bb2b8,#6b4c48)" role="img" aria-label="Stacked shipping containers at a port">Logistic</div>

  <a class="abs btn svc-btn">View All Service</a>
</section>

<section class="reviews" role="img" aria-label="City skyline at dusk behind client reviews">
  <h2 class="abs h2 reviews-title">What Client Say About Steadfast</h2>

  <article class="review" style="left:117px">
    <p>Sales person was the primary reason I choose Steadfast, The driver and his partner were right on top of everything from the packing of the truck to the unloading storage of my goods.</p>
    <div class="review-meta"><span class="avatar"></span><div><div class="review-date">March 22, 2022</div><div class="review-name">Martin R.</div></div>
      <div class="stars"><svg width="126" height="20" viewBox="0 0 126 20" fill="#76c51f"><polygon points="10,1 12.6,7 19,7.4 14,11.6 15.6,18 10,14.5 4.4,18 6,11.6 1,7.4 7.4,7"/><polygon transform="translate(26 0)" points="10,1 12.6,7 19,7.4 14,11.6 15.6,18 10,14.5 4.4,18 6,11.6 1,7.4 7.4,7"/><polygon transform="translate(52 0)" points="10,1 12.6,7 19,7.4 14,11.6 15.6,18 10,14.5 4.4,18 6,11.6 1,7.4 7.4,7"/><polygon transform="translate(78 0)" points="10,1 12.6,7 19,7.4 14,11.6 15.6,18 10,14.5 4.4,18 6,11.6 1,7.4 7.4,7"/><polygon transform="translate(104 0)" points="10,1 12.6,7 19,7.4 14,11.6 15.6,18 10,14.5 4.4,18 6,11.6 1,7.4 7.4,7"/></svg></div>
    </div>
  </article>
  <article class="review" style="left:631px;width:447px">
    <p>Sales person was the primary reason I choose Steadfast, The driver and his partner were right on top of everything from the packing of the truck to the unloading storage of my goods.</p>
    <div class="review-meta"><span class="avatar"></span><div><div class="review-date">March 22, 2022</div><div class="review-name">Martin R.</div></div>
      <div class="stars"><svg width="126" height="20" viewBox="0 0 126 20" fill="#76c51f"><polygon points="10,1 12.6,7 19,7.4 14,11.6 15.6,18 10,14.5 4.4,18 6,11.6 1,7.4 7.4,7"/><polygon transform="translate(26 0)" points="10,1 12.6,7 19,7.4 14,11.6 15.6,18 10,14.5 4.4,18 6,11.6 1,7.4 7.4,7"/><polygon transform="translate(52 0)" points="10,1 12.6,7 19,7.4 14,11.6 15.6,18 10,14.5 4.4,18 6,11.6 1,7.4 7.4,7"/><polygon transform="translate(78 0)" points="10,1 12.6,7 19,7.4 14,11.6 15.6,18 10,14.5 4.4,18 6,11.6 1,7.4 7.4,7"/><polygon transform="translate(104 0)" points="10,1 12.6,7 19,7.4 14,11.6 15.6,18 10,14.5 4.4,18 6,11.6 1,7.4 7.4,7"/></svg></div>
    </div>
  </article>
  <article class="review" style="left:1145px">
    <p>Sales person was the primary reason I choose Steadfast, The driver and his partner were right on top.</p>
    <div class="review-meta"><span class="avatar"></span></div>
  </article>

  <span class="dot on" style="left:557px"></span>
  <span class="dot" style="left:589px"></span>
  <span class="dot" style="left:623px"></span>
</section>

<section>
  <h2 class="abs h2 features-title">Don't Ever Hesitate To<br>Choose Us In Your<br>Goods Moving Service</h2>

  <div class="feat" style="left:131px;top:2990px">
    <svg viewBox="0 0 52 52" fill="none" stroke="#7ac943" stroke-width="2"><circle cx="20" cy="16" r="8"/><path d="M5 42c0-9 7-14 15-14s12 3 14 8"/><path d="M34 22l4 4 8-8"/></svg>
    <h3>Propessional</h3><p>Get moved with our high quality, low cost moving company.</p>
  </div>
  <div class="feat" style="left:374px;top:2990px">
    <svg viewBox="0 0 52 52" fill="none" stroke="#7ac943" stroke-width="2.5"><rect x="6" y="6" width="40" height="28" rx="2"/><path d="M6 26h40M20 34v8M32 34v8M14 44h24"/></svg>
    <h3>Local</h3><p>Get moved with our experienced and friendly local movers that will have you settled in 24 hours.</p>
  </div>
  <div class="feat" style="left:621px;top:2990px">
    <svg viewBox="0 0 52 52" fill="none" stroke="#7ac943" stroke-width="2"><circle cx="26" cy="10" r="5"/><circle cx="12" cy="16" r="4"/><circle cx="40" cy="16" r="4"/><path d="M19 40V24h14v16M7 36V24h8M45 36V24h-8M22 40v8M30 40v8"/></svg>
    <h3>Reliable</h3><p>You can rest assured that your move will go exactly as planned.</p>
  </div>
  <div class="feat" style="left:866px;top:2990px">
    <svg viewBox="0 0 52 52" fill="none" stroke="#7ac943" stroke-width="2.5"><rect x="6" y="11" width="40" height="30" rx="3"/><path d="M6 20h40M12 32h4M19 32h4M26 32h4"/></svg>
    <h3>Transparent Pricing</h3><p>Get moved with our high quality, low cost moving company.</p>
  </div>

  <div class="feat" style="left:131px;top:3236px">
    <svg viewBox="0 0 52 52" fill="none" stroke="#7ac943" stroke-width="2"><circle cx="26" cy="26" r="20"/><ellipse cx="26" cy="26" rx="9" ry="20"/><path d="M6 26h40M9 16h34M9 36h34"/></svg>
    <h3>Realtime Tracking</h3><p>Get moved with our high quality, low cost moving company.</p>
  </div>
  <div class="feat" style="left:374px;top:3236px">
    <svg viewBox="0 0 52 52"><path d="M26 4l18 7v13c0 12-8 20-18 24C16 44 8 36 8 24V11z" fill="#7ac943"/><path d="M26 10v32c-7-3-12-9-12-18V15z" fill="#fff"/></svg>
    <h3>Security For Cargo</h3><p>Get moved with our high quality, low cost moving company.</p>
  </div>
  <div class="feat" style="left:621px;top:3236px">
    <svg viewBox="0 0 52 52" fill="none" stroke="#7ac943" stroke-width="2"><circle cx="26" cy="26" r="20"/><path d="M26 37V15M17 24l9-9 9 9"/></svg>
    <h3>Easy Payment</h3><p>Get moved with our high quality, low cost moving company.</p>
  </div>
  <div class="feat highlight" style="left:853px;top:3216px">
    <svg viewBox="0 0 52 52" fill="none" stroke="#fff" stroke-width="2"><path d="M46 6L4 22l16 7 6 17z"/><path d="M46 6L20 29"/></svg>
    <h3>Fast &amp; Efisient</h3><p>Get moved with our high quality, low cost moving company.</p>
  </div>
</section>

<section class="cta">
  <h2 class="abs cta-title">IS YOUR MOVE RIGHT<br>AROUND THE CORNER?</h2>
  <a class="abs btn cta-btn">Get A Free Quote Today</a>
</section>

<section class="partners" aria-label="Partner badges">
  <span class="badge" style="width:136px"></span>
  <span class="badge" style="width:136px"></span>
  <span class="badge" style="width:116px"></span>
  <span class="badge" style="width:132px"></span>
  <span class="badge" style="width:134px"></span>
  <span class="badge" style="width:112px"></span>
</section>

<footer class="footer">
  <div class="brand"><span class="brand-mark"></span>Steadfast Haulers</div>

  <h4 class="foot-h" style="left:455px">Quick Links</h4>
  <ul class="foot-links">
    <li>Request A Quote</li>
    <li>Track &amp; Trace</li>
    <li>Find A Location</li>
    <li>Global Agents</li>
    <li>Help &amp; FAQ</li>
    <li>Careers</li>
  </ul>

  <h4 class="foot-h" style="left:690px">Stay In Touch With Steadfast</h4>
  <p class="abs foot-text">Not ready to "MOVE" on ? JOin our mailing list to stay up to date on the latest Steadfast news.</p>
  <div class="abs subscribe"><a class="btn subscribe-btn">Join Now</a></div>

  <span class="social" style="left:690px"></span>
  <span class="social" style="left:744px"></span>
  <span class="social" style="left:797px"></span>
  <span class="social" style="left:853px"></span>
</footer>

</body>
</html>
```